Realtor/Real Estate Investor Business Card Design

We need a business card design for a new real estate company in Maryland. We buy houses, fix and sell. We do wholesaling as well. We also rent houses.We would like to have blue background and white font.
Updates

Hi All,
I thank all of you for your efforts. You are all experts in designing.
Looking forward to meeting you online in the near future.
mira

Industry/Entity Type

Real Estate

Contact Information for Business Card

Mira Talwen
Real Estate Professional
mira@brightkeyhomes.com
301-584-3092
Bright K Homes.com

Requirements
Must have
• House picture, and logo at the back of the card
We simplify your buying and selling real estate. at the back of the card

```html
<!DOCTYPE html>
<html lang="en">
<head>
<meta charset="utf-8">
<title>Mira Talwen – Business Card</title>
<link rel="stylesheet" href="https://fonts.googleapis.com/css2?family=Arimo:wght@400;700&display=swap">
<style>
  :root {
    --card-blue-light: #4192cc;
    --card-blue-mid: #2a7dbd;
    --card-blue-deep: #0a67ab;
    --ink-white: #ffffff;
    --text-shadow: rgba(0, 40, 80, 0.35);
  }
  html, body {
    margin: 0;
    padding: 0;
    width: 1200px;
    height: 702px;
    overflow: hidden;
  }
  .card {
    position: relative;
    width: 1200px;
    height: 702px;
    background: radial-gradient(ellipse 620px 420px at 600px 330px,
      var(--card-blue-light) 0%, var(--card-blue-mid) 55%, var(--card-blue-deep) 100%);
    font-family: "Arimo", Arial, sans-serif;
    color: var(--ink-white);
    overflow: hidden;
  }
  .card p { margin: 0; position: absolute; line-height: 1; white-space: nowrap; text-shadow: 0 1px 2px var(--text-shadow); }
  .name { left: 100px; top: 202px; font-size: 54px; font-weight: 700; }
  .role { left: 100px; top: 264px; font-size: 34px; font-weight: 400; }
  .email { left: 160px; top: 398px; font-size: 35px; }
  .phone { left: 160px; top: 440px; font-size: 35px; }
  .website { left: 100px; top: 528px; font-size: 35px; font-weight: 700; }
  .icon { position: absolute; }
  .icon-mail { left: 108px; top: 403px; }
  .icon-phone { left: 115px; top: 440px; }
  .house-art {
    position: absolute;
    left: 627px;
    top: 77px;
    width: 512px;
    height: 140px;
    border-radius: 50% 50% 8px 8px / 60% 60% 8px 8px;
    background: linear-gradient(180deg, rgba(255,255,255,0.85), rgba(255,255,255,0.6));
  }
</style>
</head>
<body>
  <main class="card">
    <div class="house-art" role="img" aria-label="White silhouette of houses and trees on a rolling hill"></div>

    <p class="name">Mira Talwen</p>
    <p class="role">Real Estate Professional</p>

    <svg class="icon icon-mail" width="32" height="22" viewBox="0 0 32 22" aria-hidden="true">
      <rect x="1" y="1" width="30" height="20" fill="var(--ink-white)"/>
      <path d="M1 1 L16 13 L31 1" fill="none" stroke="var(--card-blue-mid)" stroke-width="2"/>
    </svg>
    <p class="email">mira@brightkeyhomes.com</p>

    <svg class="icon icon-phone" width="22" height="32" viewBox="0 0 22 32" aria-hidden="true">
      <path d="M4 2 L9 2 L10 9 L7 11 C8 17 10 21 13 24 L16 22 L21 27 L18 31 C9 29 2 19 2 6 Z" fill="var(--ink-white)"/>
    </svg>
    <p class="phone">301-584-3092</p>

    <p class="website">www.brightkhomes.com</p>
  </main>
</body>
</html>
```